Business Card Design

Psychotherapy and Therapeutic Counselling

As well as Life Coaching.

Industry/Entity Type

Business

Contact Information for Business Card

Harbour
Life Coaching Services
Confidential and Compassionate
KT FdSc Qualified Practitioner

Tel 07481502637

```html
<!DOCTYPE html>
<html lang="en">
<head>
<meta charset="utf-8">
<title>Harbour Life Coaching Services – Business Card</title>
<link rel="stylesheet" href="https://fonts.googleapis.com/css2?family=Source+Sans+3:wght@400;600&display=swap">
<style>
  :root {
    --card-bg: #ffffff;
    --ink: #111111;
    --leaf-green: #4cb848;
    --leaf-green-light: #8fd48b;
  }
  * { margin: 0; padding: 0; box-sizing: border-box; }
  html, body {
    width: 1200px;
    height: 791px;
    overflow: hidden;
    background: var(--card-bg);
  }
  .card {
    position: relative;
    width: 1200px;
    height: 791px;
    background: var(--card-bg);
    color: var(--ink);
    font-family: "Source Sans 3", "Myriad Pro", sans-serif;
    overflow: hidden;
  }
  .leaf-field {
    position: absolute;
    inset: 0;
    width: 1200px;
    height: 791px;
    z-index: 0;
  }
  .contact {
    position: absolute;
    left: 35px;
    top: 88px;
    z-index: 1;
  }
  .contact__business {
    font-size: 48px;
    font-weight: 600;
    line-height: 48px;
    margin-bottom: 8px;
    white-space: nowrap;
  }
  .contact__line {
    font-size: 46px;
    font-weight: 400;
    line-height: 58px;
    white-space: nowrap;
  }
  .services {
    position: absolute;
    left: 35px;
    top: 655px;
    z-index: 1;
  }
  .services__tagline {
    font-size: 43px;
    font-weight: 600;
    line-height: 49px;
    white-space: nowrap;
  }
  .services__list {
    font-size: 42px;
    font-weight: 400;
    line-height: 49px;
    white-space: nowrap;
  }
</style>
</head>
<body>
  <div class="card">
    <svg class="leaf-field" viewBox="0 0 1200 791" role="img" aria-label="Scattered green leaf pattern along the right side of the card">
      <defs>
        <linearGradient id="leaf-fade" x1="0" y1="0" x2="1" y2="0">
          <stop offset="0" stop-color="var(--leaf-green-light)" stop-opacity="0.55"/>
          <stop offset="0.6" stop-color="var(--leaf-green)" stop-opacity="0.8"/>
          <stop offset="1" stop-color="var(--leaf-green)" stop-opacity="0.9"/>
        </linearGradient>
      </defs>
      <path fill="url(#leaf-fade)"
            d="M612,0 L1200,0 L1200,791 L870,791 C885,700 950,620 965,520 C980,420 960,300 985,190 C995,110 820,50 612,0 Z"/>
    </svg>

    <section class="contact">
      <h1 class="contact__business">Harbour Life Coaching Services</h1>
      <p class="contact__line">KT FdSc Qualified Practitioner</p>
      <p class="contact__line">t: 07481502637</p>
      <p class="contact__line">e: xxxx@xxxx.net</p>
    </section>

    <section class="services">
      <p class="services__tagline">Confidential and Compassionate</p>
      <p class="services__list">Psychotherapy . Therapeutic Counselling . Life Coaching</p>
    </section>
  </div>
</body>
</html>
```